Business Card Design - Service Company

Use of the card mainly in living rooms and relations b2b We wish a card with a modern design, blue tones in the background would be a plus The card must be front / back (one side with the logo / the other with the information of contact )

Font styles to use
Serif

Requirements
Must have
• Using the map on the back of the business card Editable format! Photoshop CS2 / Illustrator CS2
Nice to have
• Maquis Vertex IT Pierre Blanche Commercial Center, 20480 Lorvanu 0495718243 Siret 71384096200018 APE 6203Y https://www.fb.com/ateliertech.maquisvertex www.maquis-vertex.com

```html
<!DOCTYPE html>
<html lang="en">
<head>
<meta charset="utf-8">
<title>Maquis Vertex IT — Business Card</title>
<link rel="stylesheet" href="https://fonts.googleapis.com/css2?family=Arimo:wght@400;700&display=swap">
<style>
  :root {
    --navy: #0d131d;
    --navy-row: #141c28;
    --row-line: #273241;
    --mint: #66f0c0;
    --blue: #3a80b6;
    --sky: #3d9ae6;
    --white: #ffffff;
    --text-light: #e8edf2;
    --page: #f3f3f1;
  }
  * { box-sizing: border-box; margin: 0; padding: 0; }
  html, body { width: 1200px; height: 1142px; overflow: hidden; }
  body { background: var(--page); font-family: "Arimo", Arial, sans-serif; position: relative; }

  .card { position: absolute; top: 0; height: 342px; overflow: hidden; }

  /* Front side */
  .card-front { left: 0; width: 601px; background: var(--navy); }
  .stripe { position: absolute; left: 0; width: 100%; height: 17px; background: var(--mint); }
  .stripe::after { content: ""; position: absolute; left: 177px; width: 246px; top: 0; bottom: 0; background: var(--blue); }
  .stripe-top { top: 20px; }
  .stripe-bottom { top: 303px; }

  .brand {
    position: absolute; display: flex; align-items: center; gap: 10px;
    font-weight: 700; font-size: 26px; letter-spacing: 0.5px; color: var(--sky); white-space: nowrap;
  }
  .brand-mark { width: 14px; height: 14px; background: var(--sky); flex: none; }
  .card-front .brand { left: 50%; top: 171px; transform: translate(-50%, -50%); }

  /* Back side */
  .card-back { left: 601px; width: 599px; background: var(--white); }
  .card-back .brand { left: 150px; top: 171px; transform: translate(-50%, -50%); font-size: 22px; }

  .contact-list { position: absolute; left: 299px; top: 0; width: 300px; height: 342px; list-style: none; background: var(--navy-row); }
  .contact-item { display: flex; height: 68.4px; border-bottom: 2px solid var(--row-line); }
  .contact-item:last-child { border-bottom: none; }
  .contact-icon { width: 55px; flex: none; display: flex; align-items: center; justify-content: center; background: var(--mint); }
  .contact-item:nth-child(even) .contact-icon { background: var(--blue); }
  .contact-icon .ring { width: 36px; height: 36px; border-radius: 50%; background: var(--white); display: flex; align-items: center; justify-content: center; }
  .contact-icon svg { width: 20px; height: 20px; }
  .contact-text { padding: 0 10px 0 13px; display: flex; align-items: center; color: var(--text-light); font-size: 12.5px; line-height: 1.4; }
  .contact-text.address { align-items: flex-start; padding-top: 18px; }
  .contact-text.small { font-size: 10.5px; }
</style>
</head>
<body>

<section class="card card-front" aria-label="Card front">
  <div class="stripe stripe-top"></div>
  <div class="brand"><span class="brand-mark"></span>Maquis Vertex IT</div>
  <div class="stripe stripe-bottom"></div>
</section>

<section class="card card-back" aria-label="Card back">
  <div class="brand"><span class="brand-mark"></span>Maquis Vertex IT</div>

  <ul class="contact-list">
    <li class="contact-item">
      <span class="contact-icon"><span class="ring">
        <svg viewBox="0 0 24 24" fill="none" stroke="#66f0c0" stroke-width="2.4"><path d="M12 22s7-7.2 7-12.5A7 7 0 0 0 5 9.5C5 14.8 12 22 12 22z"/><circle cx="12" cy="9.5" r="2.5"/></svg>
      </span></span>
      <span class="contact-text address">Pierre Blanche Commercial Center,<br>20480 Lorvanu</span>
    </li>
    <li class="contact-item">
      <span class="contact-icon"><span class="ring">
        <svg viewBox="0 0 24 24" fill="none" stroke="#3a80b6" stroke-width="2.2" stroke-linejoin="round"><path d="M6.5 3.5l3 3.5-2 2.2a11 11 0 0 0 7.3 7.3l2.2-2 3.5 3-2 2.5C11 20 4 13 4 5.5z"/></svg>
      </span></span>
      <span class="contact-text">0495718243</span>
    </li>
    <li class="contact-item">
      <span class="contact-icon"><span class="ring">
        <svg viewBox="0 0 24 24" fill="none" stroke="#66f0c0" stroke-width="2.2" stroke-linejoin="round"><rect x="3.5" y="6" width="17" height="12" rx="1"/><path d="M3.5 6.5l8.5 7 8.5-7"/></svg>
      </span></span>
      <span class="contact-text">Siret 71384096200018 6203Y</span>
    </li>
    <li class="contact-item">
      <span class="contact-icon"><span class="ring">
        <svg viewBox="0 0 24 24" fill="none" stroke="#3a80b6" stroke-width="2"><circle cx="12" cy="12" r="8.5"/><path d="M3.5 12h17M12 3.5c2.6 2.5 2.6 14.5 0 17M12 3.5c-2.6 2.5-2.6 14.5 0 17"/></svg>
      </span></span>
      <span class="contact-text">www.maquis-vertex.com</span>
    </li>
    <li class="contact-item">
      <span class="contact-icon"><span class="ring">
        <svg viewBox="0 0 24 24" fill="none" stroke="#66f0c0" stroke-width="2.2"><rect x="5" y="5" width="14" height="14" rx="2"/></svg>
      </span></span>
      <span class="contact-text small">https://www.fb.com/ateliertech.maquisvertex</span>
    </li>
  </ul>
</section>

</body>
</html>
```